Flash Website Intro
Animated flash intro for existing website with skip to site button
Hi Mira,
I sent you a private message regarding the updated link of my entry. Thanks
Tobin
Thank you for all your great work
I will now go through them with my partner and will let you know the decision
thanks
@Project Holder
Please check your private message and view my animation please.
http://vexloop.example/serve/5517302
Thanks
RunaFeld
dear sir,
i send link in private message. in that some clarity missing but real one is crystal clear
Hi PH, I sent you 2 link for #9
I sent you the link via private message.
for my entry#7
Hi,
Have you seen the animated version of my entry #5? I sent you the link via private message.
It is against the t&c's to send email address.
If you can upload to the internet and send me a link to view animation.
I won't be able to pick a design just from a static screenshot so please send me a link to view the full animation
thanks,
it's possible to see the animated result but we need to have ur personnal e-mail cauz here we cannot upload file larger than 2 mb . that's why
I have another doubt, banner or intro web, because I do not close their sizes
.gif format work here.
Hi
I have asked support how I view the animation rather than just a screenshot. Haven't had a response yet.
If anyone knows how I can view the flash files before I choose one please let me know
Hey i few questions:
How can uploads the swf´s
Or you want to take a screencapture of the intro.
Thank u
Please ignore the "Ad Sizes Required:" in the brief as it is just one flash banner size 880 x 325 (same as the white box on the home page of the website)

```html
<!DOCTYPE html>
<html lang="en">
<head>
<meta charset="utf-8">
<title>Welcome Intro Banner</title>
<link rel="stylesheet" href="https://fonts.googleapis.com/css2?family=Audiowide&display=swap">
<style>
  :root {
    --bg-edge: #cfe8b8;
    --bg-mid: #c8e5ab;
    --bg-light: #e4f2d2;
    --bar-white: #ffffff;
    --glow-warm: rgba(250, 238, 186, 0.75);
    --glow-white: rgba(255, 253, 240, 0.55);
    --letter-top: #b4e0b0;
    --letter-mid: #8ccb8e;
    --letter-bottom: #5fae6c;
    --letter-stroke: #3b8650;
  }
  html, body {
    margin: 0;
    padding: 0;
    overflow: hidden;
    background: var(--bg-edge);
  }
  .intro-banner {
    position: relative;
    width: 1200px;
    height: 444px;
    overflow: hidden;
    background: linear-gradient(180deg, var(--bg-light) 0%, var(--bg-mid) 60%, var(--bg-edge) 100%);
  }
  .intro-banner__panel {
    position: absolute;
    left: 180px;
    top: 0;
    width: 895px;
    height: 444px;
    background: radial-gradient(ellipse at 50% 45%, #e9f5da 0%, #d3ebbc 55%, #c5e3a9 100%);
  }
  .light-streaks {
    position: absolute;
    left: 0;
    top: 170px;
    width: 1200px;
    height: 170px;
    background:
      radial-gradient(ellipse 60% 30% at 50% 55%, var(--glow-warm), rgba(250, 238, 186, 0) 70%),
      linear-gradient(180deg, rgba(255, 253, 240, 0) 0%, var(--glow-white) 45%, var(--glow-warm) 60%, rgba(250, 238, 186, 0) 100%);
    opacity: 0.85;
  }
  .side-bar {
    position: absolute;
    top: 0;
    height: 444px;
    background: var(--bar-white);
  }
  .side-bar--left-wide   { left: 67px;   width: 19px; }
  .side-bar--left-thin   { left: 104px;  width: 12px; }
  .side-bar--right-wide  { left: 1085px; width: 19px; }
  .side-bar--right-thin  { left: 1128px; width: 13px; }
  .intro-banner__title {
    position: absolute;
    inset: 0;
    width: 1200px;
    height: 444px;
  }
  .welcome-title {
    font-family: "Audiowide", "Arial Black", sans-serif;
  }
</style>
</head>
<body>
  <div class="intro-banner">
    <div class="intro-banner__panel"></div>
    <div class="light-streaks" role="img" aria-label="Soft flowing light streaks in cream and white across the banner"></div>

    <div class="side-bar side-bar--left-wide"></div>
    <div class="side-bar side-bar--left-thin"></div>
    <div class="side-bar side-bar--right-wide"></div>
    <div class="side-bar side-bar--right-thin"></div>

    <svg class="intro-banner__title" viewBox="0 0 1200 444" xmlns="http://www.w3.org/2000/svg">
      <defs>
        <linearGradient id="letter-fill" x1="0" y1="0" x2="0" y2="1">
          <stop offset="0" stop-color="var(--letter-top)"/>
          <stop offset="0.5" stop-color="var(--letter-mid)"/>
          <stop offset="1" stop-color="var(--letter-bottom)"/>
        </linearGradient>
        <filter id="glossy-bevel" filterUnits="userSpaceOnUse" x="150" y="100" width="950" height="220">
          <feGaussianBlur in="SourceAlpha" stdDeviation="3.5" result="blur"/>
          <feSpecularLighting in="blur" surfaceScale="5" specularConstant="1" specularExponent="22" lighting-color="#ffffff" result="spec">
            <fePointLight x="600" y="-150" z="260"/>
          </feSpecularLighting>
          <feComposite in="spec" in2="SourceAlpha" operator="in" result="specIn"/>
          <feComposite in="SourceGraphic" in2="specIn" operator="arithmetic" k1="0" k2="1" k3="0.75" k4="0" result="lit"/>
          <feGaussianBlur in="SourceAlpha" stdDeviation="3" result="shadowBlur"/>
          <feOffset in="shadowBlur" dx="4" dy="5" result="shadowOff"/>
          <feFlood flood-color="#3f6f3a" flood-opacity="0.5"/>
          <feComposite in2="shadowOff" operator="in" result="shadow"/>
          <feMerge>
            <feMergeNode in="shadow"/>
            <feMergeNode in="lit"/>
          </feMerge>
        </filter>
      </defs>
      <text class="welcome-title" x="204" y="259" textLength="833" lengthAdjust="spacingAndGlyphs"
            font-size="138" fill="url(#letter-fill)" stroke="var(--letter-stroke)" stroke-width="3.5"
            stroke-linejoin="round" filter="url(#glossy-bevel)">WELCOME</text>
    </svg>
  </div>
</body>
</html>
```